Two (2) Merchant Advance Banner Ads

I need two (2) ads with rotating gif with 3 transitions for http://lendorbit.com/

Ad Specs:
Ad 1 must be an image equal to 250x250 pixels for website and email newsletter. .jpg, .gif, and
.png okay. No Flash!

Ad 2 must be an image equal to 720x90 pixels for website and mobile device view. .jpg, .gif, and
.png only. No Flash!

Client: Marlowe Funding Partners merchant cash advance company out of Chicago. They provide alternative (to a bank loan) financing for small business owners across the U.S.
Here's their website: www.marlowefp.com

Purpose: Recruit 3rd party sellers of alternative financing. There are many sales financing professionals already out there soliciting small businesses, we want them to make a decision to sell Marlowe's financing product to small businesses.

Copy:
Real People.
Competitive Commissions.
Great Rates.

I would like the logo (attached), phone number and CTA button to appear on all three transitions.
Call (888) 471-2859
Button: Get Started

Style:
Either something clean and simple, or something similar (not identifcal) to ads attached.
Brand standards guide is attached. Please use colors from guide.

```html
<!DOCTYPE html>
<html lang="en">
<head>
<meta charset="utf-8">
<title>Marlowe Funding Partners – Banner Ad Frames</title>
<link href="https://fonts.googleapis.com/css2?family=Source+Sans+3:wght@300;400;600;700&display=swap" rel="stylesheet">
<style>
  :root {
    --stage: #000000;
    --olive: #7d8a2e;
    --olive-dark: #6d7a24;
    --olive-glow: #c9d08f;
    --bubble-fill: #f1f1f0;
    --bubble-edge: #a7a8a6;
    --green: #7fb236;
    --navy: #4a4d72;
    --lime: #b6c22f;
    --teal: #17a0ab;
    --teal-edge: #e8f3f3;
    --slate: #3e4a5a;
    --white: #ffffff;
    --figure-shirt: #dcdcdc;
  }
  * { box-sizing: border-box; margin: 0; padding: 0; }
  html, body {
    width: 1200px; height: 450px; overflow: hidden;
    background: var(--stage);
    font-family: "Source Sans 3", Arial, sans-serif;
  }
  .board { position: relative; width: 1200px; height: 450px; }

  .ad-frame {
    position: absolute; top: 29px; width: 360px; height: 360px; overflow: hidden;
    background:
      radial-gradient(circle at 28% 58%, var(--olive-glow) 0%, rgba(201,208,143,0.35) 22%, rgba(125,138,46,0) 48%),
      linear-gradient(180deg, var(--olive) 0%, var(--olive-dark) 100%);
  }
  .ad-frame--1 { left: 34px; }
  .ad-frame--2 { left: 418px; }
  .ad-frame--3 { left: 803px; }

  .frame-label {
    position: absolute; top: 404px; width: 360px; text-align: center;
    color: var(--white); font-weight: 300; font-size: 22px; letter-spacing: 0.5px;
  }

  .spokesperson {
    position: absolute; left: 10px; top: 4px; width: 172px; height: 300px;
    border-radius: 60px 60px 10px 10px;
    background: linear-gradient(180deg, #a8583a 0%, #e9c9ae 22%, var(--figure-shirt) 38%, var(--figure-shirt) 85%, #2a2320 100%);
    opacity: 0.85;
  }

  .bubble {
    position: absolute;
    background: var(--bubble-fill);
    border: 3px solid var(--bubble-edge);
    border-radius: 12px;
    box-shadow: 2px 3px 5px rgba(0,0,0,0.25);
    line-height: 0.95;
    text-align: center;
  }
  .bubble::before {
    content: ""; position: absolute; left: -11px; bottom: 10px;
    width: 18px; height: 18px; background: var(--bubble-fill);
    border-left: 3px solid var(--bubble-edge); border-bottom: 3px solid var(--bubble-edge);
    transform: skewY(-35deg) rotate(0deg);
  }
  .bubble--people { left: 190px; top: 16px; width: 114px; height: 67px; padding-top: 8px; }
  .bubble--commissions { left: 214px; top: 97px; width: 158px; height: 70px; padding: 16px 22px 0 10px; text-align: left; }
  .bubble--rates { left: 189px; top: 178px; width: 132px; height: 75px; padding-top: 9px; }

  .bubble__strong { display: block; font-weight: 700; }
  .bubble__light { display: block; font-weight: 300; }
  .bubble--people .bubble__strong { color: var(--green); font-size: 29px; }
  .bubble--people .bubble__light { color: var(--green); font-size: 21px; }
  .bubble--commissions .bubble__strong { color: var(--navy); font-size: 17px; }
  .bubble--commissions .bubble__light { color: var(--navy); font-size: 15px; margin-top: 2px; }
  .bubble--rates .bubble__strong { color: var(--lime); font-size: 27px; }
  .bubble--rates .bubble__light { color: var(--lime); font-size: 30px; }

  .call {
    position: absolute; left: 156px; top: 264px; width: 193px; text-align: center; color: var(--white);
  }
  .call__label { display: block; font-size: 13px; font-weight: 600; letter-spacing: 5px; }
  .call__number { display: block; font-size: 19px; font-weight: 600; margin-top: 1px; }

  .cta {
    position: absolute; left: 156px; top: 310px; width: 193px; height: 40px;
    background: var(--teal); border: 2px solid var(--teal-edge); border-radius: 6px;
    color: var(--white); font-weight: 700; font-size: 24px;
    display: flex; align-items: center; justify-content: center;
    box-shadow: 1px 2px 4px rgba(0,0,0,0.3);
  }

  .brand-panel { position: absolute; left: 0; bottom: 0; width: 170px; height: 85px; }
  .brand-name {
    position: absolute; left: 14px; bottom: 12px; width: 130px;
    color: var(--slate); font-weight: 600; font-size: 15px; line-height: 1.05;
  }
</style>
</head>
<body>
<main class="board">

  <section class="ad-frame ad-frame--1">
    <div class="spokesperson" role="img" aria-label="Illustrated businessman in glasses and tie raising one finger"></div>
    <div class="bubble bubble--people"><span class="bubble__strong">REAL</span><span class="bubble__light">PEOPLE.</span></div>
    <p class="call"><span class="call__label">CALL</span><span class="call__number">(888) 471-2859</span></p>
    <svg class="brand-panel" viewBox="0 0 170 85" aria-hidden="true"><path d="M0 85 L0 38 Q45 2 118 18 Q152 28 166 85 Z" fill="#ffffff"/></svg>
    <p class="brand-name">Marlowe Funding Partners</p>
    <div class="cta">GET STARTED</div>
  </section>
  <p class="frame-label" style="left:34px">FRAME 1</p>

  <section class="ad-frame ad-frame--2">
    <div class="spokesperson" role="img" aria-label="Illustrated businessman in glasses and tie raising two fingers"></div>
    <div class="bubble bubble--people"><span class="bubble__strong">REAL</span><span class="bubble__light">PEOPLE.</span></div>
    <div class="bubble bubble--commissions"><span class="bubble__strong">COMPETITIVE</span><span class="bubble__light">COMMISSIONS.</span></div>
    <p class="call"><span class="call__label">CALL</span><span class="call__number">(888) 471-2859</span></p>
    <svg class="brand-panel" viewBox="0 0 170 85" aria-hidden="true"><path d="M0 85 L0 38 Q45 2 118 18 Q152 28 166 85 Z" fill="#ffffff"/></svg>
    <p class="brand-name">Marlowe Funding Partners</p>
    <div class="cta">GET STARTED</div>
  </section>
  <p class="frame-label" style="left:418px">FRAME 2</p>

  <section class="ad-frame ad-frame--3">
    <div class="spokesperson" role="img" aria-label="Illustrated businessman in glasses and tie raising three fingers"></div>
    <div class="bubble bubble--people"><span class="bubble__strong">REAL</span><span class="bubble__light">PEOPLE.</span></div>
    <div class="bubble bubble--commissions"><span class="bubble__strong">COMPETITIVE</span><span class="bubble__light">COMMISSIONS.</span></div>
    <div class="bubble bubble--rates"><span class="bubble__strong">GREAT</span><span class="bubble__light">RATES.</span></div>
    <p class="call"><span class="call__label">CALL</span><span class="call__number">(888) 471-2859</span></p>
    <svg class="brand-panel" viewBox="0 0 170 85" aria-hidden="true"><path d="M0 85 L0 38 Q45 2 118 18 Q152 28 166 85 Z" fill="#ffffff"/></svg>
    <p class="brand-name">Marlowe Funding Partners</p>
    <div class="cta">GET STARTED</div>
  </section>
  <p class="frame-label" style="left:803px">FRAME 3</p>

</main>
</body>
</html>
```